Business cards for start-up accounting firm

I'm looking for a double sided business card ready for upload into Lumo print or similar print providers with no modification required by me.
I'm looking for something simple as i think cards that are too 'busy' actually detract from the message. I have some thoughts but more than happy to see what comes up. The logo i have came out of left field and i love it the moment i saw it!

My thoughts:

Side 1: Just the logo, perhaps on a dark grey or charcoal background to make the logo colours stand out?

Side 2: The call to action from me website 'Looking for a more relaxed, friendly and interactive relationship with your accountant?' with my contact information
Name: Gus Tarrow
Email: gus@ledgerowl.com.au
Website: www.ledgerowl.com.au
Phone: 1300 762 349

The call to action needs to be the first thing they see when they look at side 2. If it helps to know what we do and how we do it there is a draft website at www.ledgerowl.com.au

Like i said, happy to consider anything that comes up :)

Target Market(s)

i'm targeting small business owners who experience a lot of stress around finacial reporting and have had bad experiences with accountants in the past.

Industry/Entity Type

Accounting

Contact Information for Business Card

Contained in the Description

Font styles to use
Serif
Sans Serif
Other font styles liked:
• See logo files attached

Colors
474747

Requirements
Must have
• My logo, slogan and contact information

```html
<!DOCTYPE html>
<html lang="en">
<head>
<meta charset="utf-8">
<title>Ledger Owl – Business Cards</title>
<link rel="stylesheet" href="https://fonts.googleapis.com/css2?family=Open+Sans:wght@400;600;700&family=Ubuntu:wght@400;500;700&display=swap">
<style>
  :root {
    --purple: #833677;
    --yellow: #fcd405;
    --white: #ffffff;
    --backdrop: #e9e6e3;
    --card-shadow: rgba(0, 0, 0, 0.18);
  }
  * { box-sizing: border-box; margin: 0; padding: 0; }
  html, body { width: 1200px; height: 900px; overflow: hidden; }
  body {
    position: relative;
    background: var(--backdrop);
    font-family: "Open Sans", Arial, sans-serif;
  }
  .card {
    position: absolute;
    background: var(--white);
    box-shadow: 0 4px 14px var(--card-shadow);
    overflow: hidden;
  }
  .card--front { left: 65px; top: 42px; width: 607px; height: 370px; }
  .card--back  { left: 388px; top: 505px; width: 567px; height: 352px; }

  .holder-name {
    position: absolute; top: 36px; left: 0; width: 100%;
    text-align: center;
    font-size: 22px; font-weight: 700; color: var(--purple);
  }

  .brand { position: absolute; left: 0; width: 100%; text-align: center; }
  .card--front .brand { top: 128px; }
  .card--back .brand { top: 130px; }
  .brand-name {
    font-family: "Ubuntu", Arial, sans-serif;
    font-weight: 700; color: var(--purple);
    font-size: 60px; line-height: 1; letter-spacing: 1px;
  }
  .card--back .brand-name { font-size: 66px; }
  .tagline {
    display: flex; align-items: center; justify-content: center; gap: 10px;
    margin-top: 22px;
    font-family: "Ubuntu", Arial, sans-serif;
    font-size: 12.5px; letter-spacing: 1.6px; color: var(--purple);
    text-transform: uppercase;
  }
  .card--back .tagline { margin-top: 34px; font-size: 14px; }
  .tagline::before, .tagline::after {
    content: ""; width: 34px; height: 1px; background: var(--purple);
  }
  .card--back .tagline::before, .card--back .tagline::after { width: 38px; }

  .band { position: absolute; left: 0; top: 0; }

  .contact {
    position: absolute; left: 0; top: 270px; width: 100%;
    list-style: none; text-align: center;
    color: var(--white); font-size: 16px; line-height: 26px;
  }
  .contact li { display: flex; align-items: center; justify-content: center; gap: 5px; }
  .contact .icon { width: 13px; height: 13px; }
</style>
</head>
<body>

<section class="card card--front" aria-label="Card front with contact details">
  <svg class="band" width="607" height="370" viewBox="0 0 607 370">
    <path d="M105,266 Q330,226 607,256 L607,290 Q330,236 105,266 Z" fill="var(--yellow)"/>
    <path d="M0,270 Q300,238 607,288 L607,370 L0,370 Z" fill="var(--purple)"/>
  </svg>
  <h1 class="holder-name">Gus Tarrow</h1>
  <div class="brand">
    <div class="brand-name">Ledger Owl</div>
    <div class="tagline">Calm books, clear profit</div>
  </div>
  <ul class="contact">
    <li>
      <svg class="icon" viewBox="0 0 24 24"><path fill="var(--white)" d="M6.6 10.8a15.1 15.1 0 0 0 6.6 6.6l2.2-2.2a1 1 0 0 1 1-.25 11.4 11.4 0 0 0 3.6.57 1 1 0 0 1 1 1V20a1 1 0 0 1-1 1A17 17 0 0 1 3 4a1 1 0 0 1 1-1h3.5a1 1 0 0 1 1 1c0 1.25.2 2.45.57 3.57a1 1 0 0 1-.25 1z"/></svg>
      1300 762 349
    </li>
    <li>
      <svg class="icon" viewBox="0 0 24 24"><rect x="2" y="5" width="20" height="14" fill="var(--white)"/><path d="M2.5 5.5 12 13l9.5-7.5" fill="none" stroke="var(--purple)" stroke-width="1.8"/></svg>
      gus@ledgerowl.com.au
    </li>
    <li>
      <svg class="icon" viewBox="0 0 24 24"><circle cx="12" cy="12" r="10" fill="var(--white)"/><path d="M2 12h20M12 2c3 3 3 17 0 20M12 2c-3 3-3 17 0 20" fill="none" stroke="var(--purple)" stroke-width="1.5"/></svg>
      www.ledgerowl.com.au
    </li>
  </ul>
</section>

<section class="card card--back" aria-label="Card back with brand name">
  <div class="brand">
    <div class="brand-name">Ledger Owl</div>
    <div class="tagline">Calm books, clear profit</div>
  </div>
</section>

</body>
</html>
```